Profile Card Layout/Design Template

We recently ran a workshop with a client and during that workshop we developed some typical profiles of their target audience using flip chart paper. We now want to turn the profiles into professionally designed A5 cards we can then print and give to the client, therefore we require the profile card layout template to be designed so that in the future we can insert the profile data and images in-house.
Attached are 3 files.
1. persona_sallysocial.jpg is one of profiles we want to convert
2. profilecards.png is an example of the type of design/layout we need to convert the flip chart data to.
3. our company logo
So the layout needs to provide space for
- the profile data specified in persona_sallysocial.jpg
- some additional space for a profile summary/overview not currently shown in persona_sallysocial.jpg but
- an image/photo of the profiled person
- a placeholder for the clients logo
- a placeholder for our company logo
- placeholders for appropriate images to compliment the profile
Happy to consider both portrait and landscape designs
Would be good but not essential if we could change colours of specific elements of the design to compliment the clients corporate colours. So for instance our current clients corporate colours are #b50700, #001739 & #000000

```html
<!DOCTYPE html>
<html lang="en">
<head>
<meta charset="utf-8">
<title>Sally Social – Profile Card</title>
<link rel="stylesheet" href="https://fonts.googleapis.com/css2?family=Archivo+Black&family=Archivo:wght@700;800&family=Cinzel:wght@700&family=Fira+Sans+Extra+Condensed:wght@400;500&display=swap">
<style>
  :root {
    --brand-red: #b50700;
    --brand-red-dark: #7d0500;
    --brand-navy: #001739;
    --brand-black: #000000;
    --accent-green: #8dc63f;
    --card-white: #ffffff;
    --card-tint: #eeeeee;
    --frame-grey: #a8a8a8;
    --text-body: #1a1a1a;
    --page-bg: #d6d6d6;
    --photo-tone-1: #9a6b45;
    --photo-tone-2: #c9a27c;
  }
  * { box-sizing: border-box; margin: 0; padding: 0; }
  html, body { width: 1200px; height: 900px; overflow: hidden; }
  body { background: var(--page-bg); position: relative; }

  .profile-card {
    position: absolute; left: 302px; top: 25px;
    width: 596px; height: 850px;
    background: linear-gradient(180deg, var(--card-white) 0%, var(--card-white) 70%, var(--card-tint) 100%);
    box-shadow: 0 6px 24px rgba(0,0,0,.25);
    overflow: hidden;
  }
  .card-header { position: absolute; left: 0; top: 0; width: 596px; height: 260px; }
  .persona-title {
    position: absolute; left: 14px; top: 30px;
    font-family: "Cinzel", "Times New Roman", serif; font-weight: 700;
    font-size: 42px; letter-spacing: .5px; color: var(--card-white);
    text-shadow: 2px 2px 3px rgba(0,0,0,.45);
    transform: rotate(-3deg); transform-origin: left bottom;
  }
  .persona-goal {
    position: absolute; left: 45px; top: 125px; width: 260px;
    font-family: "Archivo Black", Verdana, sans-serif;
    font-size: 19px; line-height: 25px; color: var(--brand-navy);
  }
  .persona-goal .goal-label { color: var(--brand-red); font-size: 26px; }

  .persona-facts {
    position: absolute; left: 45px; top: 225px; width: 250px;
    font-family: "Fira Sans Extra Condensed", "Arial Narrow", sans-serif;
    color: var(--text-body);
  }
  .fact-heading {
    font-weight: 500; font-size: 13px; color: var(--brand-red);
    text-decoration: underline; text-transform: uppercase; margin-top: 8px; line-height: 17px;
  }
  .fact-heading:first-child { margin-top: 0; }
  .fact-list { list-style: none; font-size: 12.5px; line-height: 15.6px; }
  .fact-list li::before { content: "\2022"; margin-right: 3px; }

  .studio-credit {
    position: absolute; left: 50px; top: 583px; width: 230px;
    font-family: "Archivo", Verdana, sans-serif; font-weight: 800; color: var(--brand-black);
  }
  .studio-credit .credit-line { font-size: 10px; letter-spacing: 1.6px; padding-left: 24px; }
  .studio-credit .studio-name {
    display: flex; align-items: center; gap: 8px; font-size: 11px; letter-spacing: 3.4px; margin-top: 3px;
  }
  .studio-credit .studio-mark { width: 16px; height: 16px; background: var(--accent-green); margin-top: -18px; }

  .client-logo-slot {
    position: absolute; left: 51px; top: 627px; width: 225px; height: 40px;
    background: var(--brand-black); color: var(--card-white);
    font-family: "Archivo", Verdana, sans-serif; font-weight: 800; font-size: 13px;
    display: flex; align-items: center; justify-content: center;
  }

  .photo-stack { position: absolute; left: 300px; top: 14px; width: 270px; height: 290px; }
  .photo-print {
    position: absolute; background: var(--card-white);
    box-shadow: 0 2px 6px rgba(0,0,0,.3); padding: 10px;
  }
  .photo-print .photo-fill {
    width: 100%; height: 100%;
    background: linear-gradient(135deg, var(--photo-tone-1), var(--photo-tone-2));
  }
  .photo-print.back-left { left: 4px; top: 50px; width: 220px; height: 220px; transform: rotate(-7deg); }
  .photo-print.back-right { left: 40px; top: 40px; width: 225px; height: 225px; transform: rotate(8deg); }
  .photo-main {
    position: absolute; left: 7px; top: 7px; width: 241px; height: 265px;
    background: var(--card-white); box-shadow: 0 3px 8px rgba(0,0,0,.35);
    display: flex; justify-content: center; padding-top: 118px;
    font-family: "Archivo Black", Verdana, sans-serif; font-size: 20px; color: var(--brand-black);
  }

  .profile-panel {
    position: absolute; left: 308px; top: 258px; width: 274px; height: 416px;
    background: var(--card-white); box-shadow: 0 2px 8px rgba(0,0,0,.3);
  }
  .persona-name {
    position: absolute; left: 308px; top: 292px; width: 255px; text-align: center;
    font-family: "Cinzel", "Times New Roman", serif; font-weight: 700;
    font-size: 25px; color: var(--brand-navy);
  }
  .profile-summary {
    position: absolute; left: 320px; top: 338px; width: 252px;
    font-family: "Fira Sans Extra Condensed", "Arial Narrow", sans-serif;
    font-size: 12px; line-height: 16.1px; color: var(--text-body);
  }

  .gallery-slot {
    position: absolute; left: 10px; top: 689px; width: 570px; height: 146px;
    border: 5px solid var(--frame-grey); background: var(--card-white);
    display: flex; align-items: center; justify-content: center;
    font-family: "Archivo", Verdana, sans-serif; font-weight: 800; font-size: 13.5px; color: var(--brand-black);
  }
</style>
</head>
<body>
<main class="profile-card">
  <svg class="card-header" viewBox="0 0 596 260" aria-hidden="true">
    <defs>
      <linearGradient id="headerRed" x1="0" y1="0" x2="1" y2="0">
        <stop offset="0" stop-color="#b50700"/>
        <stop offset=".7" stop-color="#d3150d"/>
        <stop offset="1" stop-color="#e63a26"/>
      </linearGradient>
      <linearGradient id="headerGrey" x1="0" y1="0" x2="1" y2="1">
        <stop offset="0" stop-color="#f6f6f6"/>
        <stop offset="1" stop-color="#cfcfcf"/>
      </linearGradient>
    </defs>
    <rect x="0" y="0" width="596" height="140" fill="url(#headerGrey)"/>
    <path d="M0 0 H596 V40 C480 70 330 72 0 110 Z" fill="url(#headerRed)"/>
    <path d="M0 110 C210 84 360 70 596 40 V58 C420 86 250 100 0 128 Z" fill="#7d0500" opacity=".85"/>
    <path d="M0 128 C250 100 420 86 596 58 V120 C420 120 260 140 0 160 Z" fill="#ffffff"/>
    <path d="M380 0 C440 40 520 60 596 70 V96 C510 90 430 60 360 0 Z" fill="#e4e4e4" opacity=".9"/>
  </svg>

  <h1 class="persona-title">Sally Social</h1>

  <p class="persona-goal"><span class="goal-label">GOAL:</span> Have Fun Being Physically Active Like Minded People.</p>

  <section class="persona-facts">
    <h2 class="fact-heading">What Motivates Me?</h2>
    <ul class="fact-list">
      <li>Friendship/Relationship</li>
      <li>Making The Most Of __________?</li>
      <li>Value For Money</li>
      <li>Fun Environment</li>
      <li>Well Organized</li>
    </ul>
    <h2 class="fact-heading">Behavior</h2>
    <ul class="fact-list">
      <li>Busy</li>
      <li>No Flashy Technology</li>
    </ul>
    <h2 class="fact-heading">Frustration/Fear/Concerns</h2>
    <ul class="fact-list">
      <li>Doesn't Like Down Time</li>
      <li>Wasting My Time</li>
      <li>Who's Looking After The Bids</li>
      <li>I Won't Be Able To Play</li>
    </ul>
    <h2 class="fact-heading">Pair Points</h2>
    <ul class="fact-list">
      <li>Things Must Just Work - Functional</li>
      <li>You Won't Be Good Enough</li>
      <li>Scared Of Being Hurt</li>
      <li>No Hit</li>
      <li>Knowledge Of Rules</li>
    </ul>
  </section>

  <div class="studio-credit">
    <p class="credit-line">DESIGNED AND POWERED BY</p>
    <p class="studio-name"><span class="studio-mark"></span>SUMMIT WORKS</p>
  </div>

  <div class="client-logo-slot">CLIENTS LOGO</div>

  <div class="profile-panel"></div>

  <div class="photo-stack">
    <div class="photo-print back-left"><div class="photo-fill" role="img" aria-label="Lifestyle photo of the profiled person"></div></div>
    <div class="photo-print back-right"><div class="photo-fill" role="img" aria-label="Second lifestyle photo of the profiled person"></div></div>
    <div class="photo-main">PHOTO</div>
  </div>

  <h2 class="persona-name">NAME</h2>

  <p class="profile-summary">PROFILE: Lorem ipsum dolor sit amet, consetetur sadipscing elitr, sed diam nonumy eirmod tempor invidunt ut labore et dolore magna aliquyam erat, sed diam voluptua. At vero eos et accusam et justo duo dolores et ea rebum. Stet clita kasd gubergren, no sea takimata sanctus est Lorem ipsum dolor sit amet. Lorem ipsum dolor sit amet, consetetur sadipscing elitr, sed diam nonumy eirmod tempor invidunt ut labore et dolore magna aliquyam erat, sed diam voluptua. At vero eos et accusam et justo duo dolores et ea rebum. Stet clita kasd gubergren, no sea takimata sanctus est Lorem ipsum dolor sit amet. Lorem ipsum dolor sit amet, consetetur sadipscing elitr, sed diam nonumy eirmod tempor invidunt ut labore et dolore magna aliquyam erat, sed diam voluptua. At vero eos et accusam et justo duo dolores et ea rebum. dolores et ea rebum. Stet clita kasd gubergren, no sea takimata sanctus est Lorem ipsum dolor sit amet.</p>

  <div class="gallery-slot">placeholders for appropriate images to compliment the profile</div>
</main>
</body>
</html>
```